Letterhead Design

We need a new Letterhead design for a 30 year old Electrical Company. We service domestic and commercial places. We have a logo recently made so to incorporate that. Using same colours or interested to see others added.
Would like to see a couple of options with all the info in letterhead, then another with info in a footnote down the bottom.

info needed to be added:

-Lic. No 48162
8/22-24 Larkin Rd, Tolvern 2087
W - brightcoilpower.com.au
T - (02) 9471 3825
M - 0427 593 168
E - info@brightcoilpower.com.au
ABN: 42 597 214 630

Electrical

```html
<!DOCTYPE html>
<html lang="en">
<head>
<meta charset="utf-8">
<title>Brightcoil Power Electrical – Letterhead</title>
<link rel="stylesheet" href="https://fonts.googleapis.com/css2?family=Lato:wght@400;700&family=Delius&display=swap">
<style>
  :root {
    --ink: #333333;
    --brand-dark: #13302b;
    --brand-orange: #f39321;
    --signature: #2b2a7e;
    --paper: #ffffff;
    --backdrop: #ecebe8;
  }
  * { box-sizing: border-box; margin: 0; padding: 0; }
  html, body { width: 1112px; height: 1200px; overflow: hidden; }
  body {
    background: var(--backdrop);
    font-family: "Lato", Arial, sans-serif;
    color: var(--ink);
    position: relative;
  }
  .letterhead {
    position: absolute;
    left: 198px; top: 90px;
    width: 704px; height: 995px;
    background: var(--paper);
    box-shadow: 0 2px 10px rgba(0,0,0,.12);
    overflow: hidden;
  }
  .brand {
    position: absolute;
    left: 43px; top: 62px;
    display: flex; align-items: center; gap: 10px;
  }
  .brand-mark {
    width: 18px; height: 18px; border-radius: 50%;
    background: var(--brand-orange);
  }
  .brand-name {
    font-size: 29px; font-weight: 700;
    color: var(--brand-dark);
    line-height: 1.1;
  }
  .contact {
    position: absolute;
    right: 44px; top: 25px;
    text-align: right;
    font-size: 14.5px;
    line-height: 19px;
  }
  .contact .company { font-weight: 700; color: var(--brand-dark); }
  .contact .label { color: var(--brand-orange); }
  .contact .gap { margin-top: 3px; }
  .contact .lines { margin-top: 6px; }
  .contact .line { display: flex; justify-content: flex-end; align-items: center; gap: 6px; }
  .contact svg { width: 14px; height: 12px; fill: var(--brand-orange); }
  .letter {
    position: absolute;
    left: 43px; top: 257px;
    width: 616px;
    font-size: 14.6px;
    line-height: 18.4px;
  }
  .salutation { font-weight: 700; font-size: 15px; margin-bottom: 21px; color: #444; }
  .letter p.body { text-align: justify; margin-bottom: 18px; color: #444; }
  .closing { margin-top: 42px; color: #222; }
  .signature {
    font-family: "Delius", cursive;
    font-size: 28px; color: var(--signature);
    margin: 2px 0 10px;
    line-height: 34px;
  }
  .footer-wave { position: absolute; left: 0; bottom: 0; width: 704px; height: 80px; display: block; }
  .footer-web {
    position: absolute;
    right: 61px; bottom: 9px;
    color: #ffffff; font-size: 14.5px; letter-spacing: .3px;
  }
</style>
</head>
<body>
  <div class="letterhead">
    <div class="brand">
      <span class="brand-mark"></span>
      <span class="brand-name">Brightcoil Power</span>
    </div>

    <div class="contact">
      <div class="company">Brightcoil Power Electrical</div>
      <div>8/22-24 Larkin Rd, Tolvern 2087</div>
      <div class="gap"><span class="label">Lic. No</span>: 48162</div>
      <div><span class="label">ABN</span>: 42 597 214 630</div>
      <div class="lines">
        <div class="line">(02) 9471 3825
          <svg viewBox="0 0 14 12" aria-hidden="true"><path d="M1 4 C1 1 13 1 13 4 L10 5 L9 3 L5 3 L4 5 Z M3 6 H11 L12 11 H2 Z"/></svg></div>
        <div class="line">0427 593 168
          <svg viewBox="0 0 14 12" aria-hidden="true"><path d="M4 0 H10 V12 H4 Z M5 1.5 V8 H9 V1.5 Z"/></svg></div>
        <div class="line">info@brightcoilpower.com.au
          <svg viewBox="0 0 14 12" aria-hidden="true"><path d="M0 2 H14 V11 H0 Z M1 3 L7 7.5 L13 3 Z" fill-rule="evenodd"/></svg></div>
      </div>
    </div>

    <div class="letter">
      <p class="salutation">Dear Mr. Dalton,</p>
      <p class="body">Lorem Ipsum is simply dummy text of the printing and typesetting industry. Lorem Ipsum has been the industry's standard dummy text ever since the 1500s, when an unknown printer took a galley of type and scrambled it to make a type specimen book. It has survived not only five centuries, but also the leap into electronic typesetting, remaining essentially unchanged.</p>
      <p class="body">The standard chunk of Lorem Ipsum used since the 1500s is reproduced below for those interested. Sections 1.10.32 and 1.10.33 from "de Finibus Bonorum et Malorum" by Tullian are also reproduced in their exact original form, accompanied by English versions from the 1914 translation by H. Penfold</p>
      <p class="body">Lorem Ipsum is simply dummy text of the printing and typesetting industry. Lorem Ipsum has been the industry's standard dummy text ever since the 1500s, when an unknown printer took a galley of type and scrambled it to make a type specimen book. It has survived not only five centuries, but also the leap into electronic typesetting, remaining essentially unchanged. It was popularised in the</p>
      <div class="closing">
        <div>Sincerely Your,</div>
        <div class="signature">your name</div>
        <div>Name Last Name</div>
        <div>Company Name</div>
      </div>
    </div>

    <svg class="footer-wave" viewBox="0 0 704 80" preserveAspectRatio="none" aria-hidden="true">
      <path d="M0 3 C120 40 250 62 380 52 C500 42 620 26 704 28 L704 80 L0 80 Z" fill="var(--brand-orange)"/>
      <path d="M0 44 C150 54 300 76 430 62 C550 49 640 40 704 42 L704 80 L0 80 Z" fill="var(--brand-dark)"/>
    </svg>
    <div class="footer-web">www.brightcoilpower.com.au</div>
  </div>
</body>
</html>
```